One page website

I'm looking for a landing page for my company. Just a brief description of our medical device technology with some images

Coding

Coded - Design and coding required

```html
<!DOCTYPE html>
<html lang="en">
<head>
<meta charset="utf-8">
<title>Veritor Medical – Solving Children's Scoliosis</title>
<link rel="stylesheet" href="https://fonts.googleapis.com/css2?family=Lato:wght@300;400;700;900&family=Montserrat:wght@400;600;800;900&family=Oswald:wght@400;500&display=swap">
<style>
:root{
  --green:#9ccc3c;
  --green-dark:#8cbf2f;
  --blue:#35a4d9;
  --blue-dark:#2a93c9;
  --paper:#f1f2ee;
  --white:#ffffff;
  --ink:#333333;
  --muted:#8c8c8c;
  --xray-dark:#0f1a1a;
  --xray-light:#9fd8d4;
}
*{margin:0;padding:0;box-sizing:border-box}
html,body{width:1200px;height:2665px;overflow:hidden;background:var(--white)}
body{position:relative;font-family:'Lato',sans-serif;color:var(--ink)}
.abs{position:absolute}

/* hero */
.hero-bg{left:0;top:0;width:1200px;height:1015px;background:var(--paper)}
.hero-photo{left:0;top:0;width:1200px;height:660px;background:linear-gradient(100deg,#e6e7ef 0%,#d9dbe6 40%,#dfe0ea 70%,#e8e9f0 100%)}
.hero-shapes{left:0;top:0}
.nav{left:179px;top:0;display:flex;gap:3px}
.nav a{display:block;width:96px;height:72px;background:var(--green);border-radius:0 0 22px 22px;color:var(--white);font-family:'Oswald',sans-serif;font-size:16px;text-decoration:none;text-align:center;padding-top:24px;letter-spacing:.3px}
.nav a span{border-bottom:1px solid var(--white);padding-bottom:2px}
.brand{left:833px;top:28px;width:272px;height:258px;border-radius:50%;background:var(--white);border:5px solid var(--green);border-top-color:transparent;border-right-color:transparent;transform:rotate(-45deg)}
.brand-name{left:833px;top:135px;width:272px;text-align:center;font-family:'Lato',sans-serif;font-weight:700;font-size:40px;line-height:1;color:var(--blue)}
.headline{left:667px;top:331px;width:533px;height:202px;background:var(--blue);border-radius:22px 0 0 0;box-shadow:0 7px 0 var(--green);padding:22px 0 0 38px;color:var(--white)}
.headline h1{font-family:'Montserrat',sans-serif;font-weight:400;font-size:42px;line-height:44px}
.headline h1 b{font-weight:900;color:var(--green)}
.headline h1 strong{font-weight:900}
.headline p{margin-top:12px;font-family:'Montserrat',sans-serif;font-size:22px;line-height:29px;color:#e6f4fb}

/* severity cards */
.card{top:655px;width:278px;height:357px;border-radius:32px;background:var(--blue);text-align:center;color:var(--white)}
.card.light{background:var(--paper);color:var(--blue)}
.card .xray{position:absolute;left:39px;top:20px;width:200px;height:200px;border-radius:50%;border:3px solid var(--white);box-shadow:0 0 0 2px var(--blue);background:radial-gradient(ellipse at 50% 45%,var(--xray-light) 0%,#4f8f8c 30%,var(--xray-dark) 70%)}
.card.light .xray{border-color:var(--white)}
.card h3{position:absolute;top:234px;left:0;width:100%;font-weight:400;font-size:25px;padding-top:8px}
.card h3:before,.card h3:after{content:"";position:absolute;left:50%;width:104px;margin-left:-52px;height:2px;background:currentColor}
.card h3:before{top:0}
.card h3:after{top:46px}
.card ul{position:absolute;left:50px;top:296px;text-align:left;font-size:14.5px;line-height:22px;list-style:none}
.card li:before{content:"•";margin-right:12px}
.card.light ul{color:#666}

/* join */
.join-boy{left:134px;top:1055px;width:192px;height:455px;border-radius:90px 90px 40px 40px;background:linear-gradient(180deg,#f2c9a8 0%,#2f8fd6 35%,#2f8fd6 55%,#7a7055 70%,#f0c2a0 100%)}
.join h2{position:absolute;left:331px;top:1110px;width:527px;text-align:center;font-weight:400;font-size:43px;color:var(--green)}
.field{left:331px;width:527px;height:43px;border:1.5px solid #c9c9c9;border-radius:22px;background:var(--white);padding-left:18px;font-size:15px;line-height:40px;color:#9a9a9a}
.btn-signup{left:331px;top:1441px;width:160px;height:44px;border-radius:22px;background:linear-gradient(180deg,#8fd29a,#6bbf84);color:var(--white);font-size:14px;text-align:center;line-height:44px}

/* procedures */
.proc-title{left:0;top:1610px;width:1200px;text-align:center;font-family:'Montserrat',sans-serif;font-weight:800;font-size:32px;color:var(--blue)}
.proc-text{left:0;top:1662px;width:1200px;text-align:center;font-size:15.5px;line-height:19px;color:#222}
.proc{top:1759px;width:270px}
.proc .shot{height:158px;background:linear-gradient(180deg,#3b3f40,#9ea3a4 50%,#4a4e4f)}
.proc .label{height:32px;line-height:32px;text-align:center;color:var(--white);font-weight:700;font-size:15px}

/* team */
.team-title{left:0;top:2130px;width:1200px;text-align:center;font-family:'Montserrat',sans-serif;font-weight:400;font-size:34px;color:var(--white);letter-spacing:.5px}
.team-title b{font-weight:900}
.team-sub{left:0;top:2182px;width:1200px;text-align:center;font-size:17px;color:var(--white)}
.member{top:2220px;width:150px;text-align:center;color:var(--white);font-size:22px;font-weight:300}
.member svg{display:block;margin:0 auto 16px}

/* footer */
.footer{left:0;top:2416px;width:1200px;height:249px;background:var(--blue)}
.foot-h{font-family:'Lato',sans-serif;font-weight:300;font-size:35px;color:var(--white);letter-spacing:-.5px}
.foot-h b{font-weight:900}
.about p{margin-top:18px;width:275px;font-size:14.5px;line-height:18px;color:var(--white)}
.links ul{list-style:none;margin-top:14px;width:198px}
.links li{font-family:'Montserrat',sans-serif;font-weight:600;font-size:13px;letter-spacing:2.8px;color:var(--white);height:26.5px;line-height:25px;border-bottom:1px solid rgba(255,255,255,.35);padding-left:26px;position:relative}
.links li:before{content:"";position:absolute;left:4px;top:8px;width:6px;height:6px;border-right:2px solid #f5c518;border-bottom:2px solid #f5c518;transform:rotate(-45deg)}
.contact{left:843px;top:2416px;width:357px;height:249px;background:var(--white);border-radius:60px 0 0 60px}
.contact .foot-h{color:var(--green);font-size:34px;margin:28px 0 0 46px}
.c-row{position:absolute;left:92px;font-size:14.5px;line-height:17px;color:var(--blue)}
.c-ico{position:absolute;left:50px}
</style>
</head>
<body>

<!-- hero -->
<div class="abs hero-bg"></div>
<div class="abs hero-photo" role="img" aria-label="Photo of a smiling young girl balancing with arms outstretched on an exercise ball while a therapist supports her feet"></div>

<svg class="abs hero-shapes" width="1200" height="1080" viewBox="0 0 1200 1080" aria-hidden="true">
  <path d="M830 0 H1200 V60 C1160 90 1120 110 1080 120 C1000 60 920 30 830 0 Z" fill="var(--paper)"/>
  <path d="M0 210 C120 120 320 85 540 88" fill="none" stroke="var(--blue)" stroke-width="9" stroke-linecap="round"/>
  <path d="M0 500 C140 600 320 650 520 630 C700 612 850 575 1000 590 C1100 600 1160 640 1200 660 V1015 H0 Z" fill="var(--green)"/>
  <path d="M0 508 C140 605 300 640 470 632" fill="none" stroke="var(--blue)" stroke-width="5"/>
  <path d="M0 1015 L600 1036 L1200 1015 L1200 1030 L600 1072 L0 1030 Z" fill="var(--blue)"/>
  <path d="M0 1030 L600 1072 L1200 1030 V1080 H0 Z" fill="var(--paper)"/>
</svg>

<nav class="abs nav">
  <a href="#"><span>OVERVIEW</span></a>
  <a href="#">APPOINTMENT</a>
  <a href="#">ABOUT US</a>
  <a href="#">LOGIN</a>
  <a href="#">SIGN UP</a>
</nav>

<div class="abs brand"></div>
<div class="abs brand-name">Veritor Medical</div>

<div class="abs headline">
  <h1>Solving <b>Children’s</b><br><strong>Scoliosis</strong></h1>
  <p>Develop novel technologies focusing<br>on non-fusion scoliosis correction</p>
</div>

<div class="abs card" style="left:178px">
  <div class="xray" role="img" aria-label="X-ray of a spine with mild curvature"></div>
  <h3>Mild scoliosis</h3>
  <ul><li>10- to 24-degree Cobb</li><li>Treatment: Monitoring</li></ul>
</div>
<div class="abs card light" style="left:460px">
  <div class="xray" role="img" aria-label="X-ray of a spine with moderate curvature"></div>
  <h3>Moderate scoliosis</h3>
  <ul><li>25- to 39-degree Cobb</li><li>Treatment: Bracing</li></ul>
</div>
<div class="abs card" style="left:743px">
  <div class="xray" role="img" aria-label="X-ray of a spine with severe curvature"></div>
  <h3>Severe scoilosis</h3>
  <ul><li>40- to 50-degree Cobb</li><li>Treatment: Fusion</li></ul>
</div>

<!-- join -->
<svg class="abs" style="left:0;top:1072px" width="1200" height="490" viewBox="0 0 1200 490" aria-hidden="true">
  <path d="M0 0 H1200 V430 L600 483 L0 430 Z" fill="var(--paper)"/>
</svg>
<div class="abs join-boy" role="img" aria-label="Photo of a happy boy in a blue t-shirt jumping with arms raised"></div>
<section class="join">
  <h2>Join Now</h2>
  <div class="abs field" style="top:1187px">First Name</div>
  <div class="abs field" style="top:1247px">Last Name</div>
  <div class="abs field" style="top:1307px">Email</div>
  <div class="abs field" style="top:1367px">Choose Your Password</div>
  <div class="abs btn-signup">SIGN UP</div>
</section>

<!-- procedures -->
<h2 class="abs proc-title">Procedures &amp; Solutions</h2>
<p class="abs proc-text">Between the Harbor Kids group and Dr. Lenhart at Westbay University Medical Center (WUMC),<br>350+ VBT these procedures and Solutions were completed.1</p>
<svg class="abs" style="left:180px;top:1727px" width="850" height="20" viewBox="0 0 850 20" aria-hidden="true">
  <line x1="0" y1="10" x2="845" y2="10" stroke="#e3e3e3" stroke-width="2"/>
  <path d="M838 5 L845 10 L838 15" fill="none" stroke="#e3e3e3" stroke-width="2"/>
  <rect x="422" y="3" width="14" height="14" fill="var(--white)" stroke="var(--blue)" stroke-width="2"/>
</svg>
<div class="abs proc" style="left:180px"><div class="shot" role="img" aria-label="Two spinal X-rays comparing a curved spine before and after fusion"></div><div class="label" style="background:var(--blue)">Fusion limitations</div></div>
<div class="abs proc" style="left:468px"><div class="shot" role="img" aria-label="Chest X-ray showing vertebral body tethering screws"></div><div class="label" style="background:var(--green)">VBT Tethering</div></div>
<div class="abs proc" style="left:755px"><div class="shot" role="img" aria-label="Lateral X-ray of an animal spine with implanted hardware"></div><div class="label" style="background:var(--green)">Pilot Pig Study</div></div>

<!-- team -->
<svg class="abs" style="left:0;top:2040px" width="1200" height="380" viewBox="0 0 1200 380" aria-hidden="true">
  <path d="M0 3 L600 60 L1200 3 V376 H0 Z" fill="var(--green)"/>
  <path d="M0 3 L600 60 L1200 3 V16 L600 78 L0 16 Z" fill="var(--blue)"/>
  <path d="M116 2208 L86 2242 L116 2276" transform="translate(0,-2040)" fill="none" stroke="var(--white)" stroke-width="5" stroke-linecap="round"/>
  <path d="M1076 2208 L1106 2242 L1076 2276" transform="translate(0,-2040)" fill="none" stroke="var(--white)" stroke-width="5" stroke-linecap="round"/>
</svg>
<h2 class="abs team-title">MEET OUR <b>TEAM MEMBERS</b></h2>
<p class="abs team-sub">Founding Team – Experience in <b>Orthopedic Implants</b></p>

<div class="abs member" style="left:178px">
  <svg width="116" height="116" viewBox="0 0 116 116"><circle cx="58" cy="58" r="54" fill="none" stroke="var(--white)" stroke-width="4" stroke-dasharray="120 20 80 20 100 20"/><circle cx="58" cy="58" r="46" fill="#8fb3d6" stroke="var(--blue)" stroke-width="3" role="img" aria-label="Portrait photo of team member"/></svg>
  Dana Whitlock</div>
<div class="abs member" style="left:354px">
  <svg width="116" height="116" viewBox="0 0 116 116"><circle cx="58" cy="58" r="54" fill="none" stroke="var(--white)" stroke-width="4" stroke-dasharray="120 20 80 20 100 20"/><circle cx="58" cy="58" r="46" fill="#8a7f80" stroke="var(--blue)" stroke-width="3" role="img" aria-label="Portrait photo of team member"/></svg>
  Ravi Mehra</div>
<div class="abs member" style="left:523px">
  <svg width="116" height="116" viewBox="0 0 116 116"><circle cx="58" cy="58" r="54" fill="none" stroke="var(--white)" stroke-width="4" stroke-dasharray="120 20 80 20 100 20"/><circle cx="58" cy="58" r="46" fill="#5b3a32" stroke="var(--blue)" stroke-width="3" role="img" aria-label="Portrait photo of team member"/></svg>
  Owen Calder</div>
<div class="abs member" style="left:694px">
  <svg width="116" height="116" viewBox="0 0 116 116"><circle cx="58" cy="58" r="54" fill="none" stroke="var(--white)" stroke-width="4" stroke-dasharray="120 20 80 20 100 20"/><circle cx="58" cy="58" r="46" fill="#4f6f8f" stroke="var(--blue)" stroke-width="3" role="img" aria-label="Portrait photo of team member"/></svg>
  Leo Brandt</div>
<div class="abs member" style="left:868px">
  <svg width="116" height="116" viewBox="0 0 116 116"><circle cx="58" cy="58" r="54" fill="none" stroke="var(--white)" stroke-width="4" stroke-dasharray="120 20 80 20 100 20"/><circle cx="58" cy="58" r="46" fill="#6e6460" stroke="var(--blue)" stroke-width="3" role="img" aria-label="Portrait photo of team member"/></svg>
  Marco Silva</div>

<!-- footer -->
<footer class="abs footer">
  <div class="abs about" style="left:79px;top:26px">
    <h3 class="foot-h">about <b>Veritor</b> Medical</h3>
    <p>Lorem ipsum dolor sit amet, consectetur adipiscing elit, sed do eiusmod tempor incididunt ut labore et dolore magna aliqua. Ut enim ad minim veniam, quis nostrud exercitation ullamco laboris nisi ut aliquip ex ea commodo consequat</p>
  </div>
  <div class="abs links" style="left:497px;top:22px">
    <h3 class="foot-h">navigate <b>links</b></h3>
    <ul>
      <li>OUR TECHNOLOGY</li>
      <li>OUR PARTNERS</li>
      <li>PRICING PLANS</li>
      <li>OUR FEATURES</li>
      <li>TERMS &amp; CONDITION</li>
    </ul>
  </div>
</footer>
<svg class="abs" style="left:818px;top:2512px" width="30" height="56" viewBox="0 0 30 56" aria-hidden="true"><path d="M30 0 L0 28 L30 56 Z" fill="var(--white)"/></svg>
<div class="abs contact">
  <h3 class="foot-h">get <b>in-touch</b></h3>
  <svg class="c-ico" style="top:97px" width="26" height="22" viewBox="0 0 26 22" aria-hidden="true"><path d="M13 1 L25 11 H21 V21 H16 V14 H10 V21 H5 V11 H1 Z" fill="var(--blue)"/></svg>
  <div class="c-row" style="top:96px">14 Maple Row,<br>Suite 3 Brookfield,</div>
  <svg class="c-ico" style="top:147px" width="22" height="28" viewBox="0 0 22 28" aria-hidden="true"><path d="M10 3 C4 6 4 22 10 25 L13 21 C10 19 10 9 13 7 Z" fill="var(--blue)"/></svg>
  <div class="c-row" style="top:146px">+440 100200300 - Office<br>+440 100200301 - Fax</div>
  <svg class="c-ico" style="top:198px" width="24" height="18" viewBox="0 0 24 18" aria-hidden="true"><rect x="1" y="1" width="22" height="16" rx="2" fill="var(--blue)"/><path d="M2 3 L12 10 L22 3" fill="none" stroke="var(--white)" stroke-width="2"/></svg>
  <div class="c-row" style="top:198px">hello@veritormed.example</div>
</div>

</body>
</html>
```